Startup Burlesque Dance Company needs logo and website

Hello designers,
We need a logo design and a website design. The company name is "Velluta Strambo". This is a rough cut of one of the company's shows: http://clipvault.example/kQ7rTmLp2Zd
The design will be for a startup Burlesque dance company. The logo and website should have a simple, retro, vintage "black and white" movie feel to it. The primary purpose for the site is for marketing the dance services, highlighting pictures and video of the show(s). There will be seven basic web pages.
• Home
• About
• Shows
• Company
• Gallery
• Promo Reel
• Contact
The following links are two examples of sites we like, but since this is a competitor, the design should not be identical. It should only serve as an example of the requested style.
http://pennybrassrevue.example/index.cfm
http://www.crookedlampcabaret.example/
In Summary, we will need the following:
1. Logo (example of ones we like are attached in Word file)
2. Web Site Design
3. Stationary ready design for business cards and letterhead
Please design to the following screen size & resolution: 1024 x 768
Reason: Decision maker has been traveling on business so our team has not been able to meet with her.
Target Market(s)
Male and Female, 21-45 years of age
Industry/Entity Type
Marketing
Look and feel

```html
<!DOCTYPE html>
<html lang="en">
<head>
<meta charset="utf-8">
<title>Velluta Strambo — Letterhead</title>
<link href="https://fonts.googleapis.com/css2?family=Rye&display=swap" rel="stylesheet">
<style>
  :root {
    --backdrop: #d6d6d6;
    --paper: #ffffff;
    --ink: #0b0b0c;
    --crimson: #a50633;
    --rule: #111111;
  }
  * { box-sizing: border-box; margin: 0; padding: 0; }
  html, body {
    width: 1200px;
    height: 1000px;
    overflow: hidden;
    background: var(--backdrop);
  }
  .letterhead {
    position: absolute;
    left: 245px;
    top: 30px;
    width: 710px;
    height: 940px;
    background: var(--paper);
  }
  .letterhead__frame {
    position: absolute;
    inset: 20px;
    border: 1.5px solid var(--rule);
    overflow: hidden;
  }
  .letterhead__header {
    position: absolute;
    left: 0;
    top: 0;
    width: 100%;
    height: 200px;
    display: block;
  }
  .letterhead__band { fill: var(--ink); }
  .letterhead__corner { fill: var(--crimson); }
  .brand-name {
    position: absolute;
    left: 24px;
    top: 30px;
    font-family: "Rye", serif;
    font-weight: 400;
    color: var(--paper);
    line-height: 1;
  }
  .brand-name__first {
    display: block;
    font-size: 42px;
    letter-spacing: 1px;
  }
  .brand-name__second {
    display: block;
    font-size: 26px;
    letter-spacing: 8px;
    margin-top: 6px;
    padding-left: 18px;
  }
  .letterhead__footer {
    position: absolute;
    left: 0;
    right: 0;
    bottom: 18px;
    text-align: center;
    font-family: "Rye", serif;
    font-variant: small-caps;
    color: var(--ink);
  }
  .contact-line {
    font-size: 11.5px;
    letter-spacing: 0.8px;
    line-height: 16px;
  }
  .contact-line--phone {
    font-size: 16px;
    letter-spacing: 1px;
    line-height: 22px;
  }
</style>
</head>
<body>
  <main class="letterhead">
    <div class="letterhead__frame">
      <svg class="letterhead__header" viewBox="0 0 668 200" preserveAspectRatio="none" aria-hidden="true">
        <path class="letterhead__band" d="M0 0 H668 V185 C630 122 515 96 385 106 C250 116 120 176 0 150 Z"/>
        <path class="letterhead__corner" d="M485 0 H668 V172 C652 100 600 55 500 30 Z"/>
      </svg>
      <h1 class="brand-name">
        <span class="brand-name__first">Velluta</span>
        <span class="brand-name__second">Strambo</span>
      </h1>
      <footer class="letterhead__footer">
        <p class="contact-line">218 Tassel Row, Limelight City, ST 00417</p>
        <p class="contact-line">www.velluta-strambo.example / em@velluta-strambo.example</p>
        <p class="contact-line contact-line--phone">(555) 017-2046</p>
      </footer>
    </div>
  </main>
</body>
</html>
```